Social Media Post Quote #4 - Native American Organization

- KINDLE - must be included
- Protect your community. Protect Your Elders. Stay Vaccinated. must be included
- Attached, company Logo, campaign logos and sample flu social media image. - our audience likes BRIGHT colors.
- Must include image from the United States, representing Land/Nature from one of the following regions, Plains and Woodlands, or Southwest, or Mountains, or Coast.
- must include quote: Our wisdom carries through generations.
- One image will be provided twice - incorporating campaign logos - in some fashion
Inspiration: https://tovrelune.org/ and https://www.facebook.com/Tovrelune

```html
<!DOCTYPE html>
<html lang="en">
<head>
<meta charset="UTF-8">
<title>KINDLE – Our wisdom carries through generations</title>
<link rel="stylesheet" href="https://fonts.googleapis.com/css2?family=Barlow+Condensed:wght@500&family=Barlow+Semi+Condensed:wght@500;600;700&display=swap">
<style>
  :root {
    --border-grey: #b9bebd;
    --border-dark: #7e8a8b;
    --sky-top: #2f7fd6;
    --sky-mid: #7fb7ec;
    --sky-low: #cfe3f3;
    --rock: #c07a4c;
    --sand: #d9a36e;
    --brush: #7f9a55;
    --panel: rgba(255, 255, 255, 0.78);
    --teal: #3a9a9c;
    --brick: #b5554b;
    --white: #ffffff;
  }
  * { margin: 0; padding: 0; box-sizing: border-box; }
  html, body { width: 1200px; height: 1200px; overflow: hidden; background: #ffffff; }
  .post {
    position: relative;
    width: 1200px;
    height: 1200px;
    overflow: hidden;
    font-family: "Barlow Semi Condensed", "Arial Narrow", sans-serif;
  }
  .frame-pattern {
    position: absolute;
    inset: 0;
    background: linear-gradient(135deg, var(--border-grey), var(--border-dark) 50%, var(--border-grey));
  }
  .landscape {
    position: absolute;
    left: 37px; top: 37px;
    width: 1126px; height: 1126px;
    background:
      radial-gradient(ellipse 40% 30% at 0% 0%, rgba(176, 96, 58, 0.9), transparent 70%),
      radial-gradient(ellipse 25% 45% at 100% 10%, rgba(176, 96, 58, 0.85), transparent 70%),
      radial-gradient(ellipse 30% 40% at 92% 62%, rgba(180, 100, 60, 0.9), transparent 70%),
      linear-gradient(180deg, var(--sky-top) 0%, var(--sky-mid) 35%, var(--sky-low) 56%, var(--rock) 62%, var(--sand) 74%, var(--brush) 88%, #6d8a48 100%);
  }
  .campaign-panel {
    position: absolute;
    left: 47px; top: 75px;
    width: 883px; height: 238px;
    background: var(--panel);
  }
  .campaign-name {
    position: absolute;
    left: 85px; top: 80px;
    font-weight: 600;
    font-size: 170px;
    line-height: 170px;
    letter-spacing: 4px;
    color: var(--teal);
  }
  .campaign-tagline {
    position: absolute;
    left: 90px; top: 256px;
    font-weight: 700;
    font-size: 22px;
    letter-spacing: 1px;
    color: var(--brick);
  }
  .org-name {
    position: absolute;
    left: 672px; top: 120px;
    width: 240px;
    font-weight: 700;
    font-size: 30px;
    line-height: 36px;
    text-transform: uppercase;
    color: var(--teal);
  }
  .call-to-action {
    position: absolute;
    left: 75px; top: 340px;
    font-weight: 600;
    font-size: 64px;
    line-height: 75px;
    color: var(--white);
    text-shadow: 0 2px 6px rgba(0, 0, 0, 0.25);
  }
  .quote {
    position: absolute;
    left: 37px; top: 590px;
    width: 1126px;
    text-align: center;
    font-family: "Barlow Condensed", "Arial Narrow", sans-serif;
    font-weight: 500;
    font-size: 185px;
    line-height: 168px;
    color: var(--white);
    text-shadow: 0 3px 10px rgba(0, 0, 0, 0.35);
  }
</style>
</head>
<body>
  <main class="post">
    <div class="frame-pattern" role="img" aria-label="Decorative zigzag woven border in grey and white"></div>
    <div class="landscape" role="img" aria-label="Southwest desert landscape with red sandstone arches and rock towers under a bright blue sky"></div>

    <div class="campaign-panel"></div>
    <div class="campaign-name">KINDLE</div>
    <div class="campaign-tagline">COVID-19 &amp; FLU VACCINATION CAMPAIGN</div>
    <div class="org-name">Tovrelune Council for Native Elders</div>

    <p class="call-to-action">
      Protect your community.<br>
      Protect Your Elders.<br>
      Stay Vaccinated.
    </p>

    <p class="quote">
      Our wisdom<br>
      carries through<br>
      generations.
    </p>
  </main>
</body>
</html>
```